Design logo and business card.

Design and construct logo and card for my business which is an over seeing company of other smaller businesses. The companies name is quarry5 business collective. Im open to any ideas but i am looking for a very cool contemporary design with a very prestige feel. The card can be either single or double sided, Thank you and i will look forward to your submissions.

Industry/Entity Type

Business

Requirements
Must have
• Company name, email, website, telephone, my name. Cool modern look with a prestige feel.

```html
<!DOCTYPE html>
<html lang="en">
<head>
<meta charset="utf-8">
<title>quarry5 business collective – business card</title>
<link rel="stylesheet" href="https://fonts.googleapis.com/css2?family=Open+Sans:wght@400&display=swap">
<style>
  :root {
    --backdrop: #ececec;
    --card: #ffffff;
    --card-edge: #9a9a9a;
    --ink: #111111;
    --ink-soft: #1c1c1c;
    --ink-light: #3a3a3a;
    --paper-text: #ffffff;
  }
  html, body {
    margin: 0;
    padding: 0;
    width: 1200px;
    height: 1000px;
    overflow: hidden;
    background: var(--backdrop);
  }
  .stage {
    display: block;
    width: 1200px;
    height: 1000px;
  }
  .card-face {
    fill: var(--card);
    stroke: var(--card-edge);
    stroke-width: 1;
  }
  .brand-name {
    font-family: "Open Sans", sans-serif;
    font-weight: 400;
  }
  .brand-name--front {
    fill: var(--paper-text);
    font-size: 68px;
  }
  .brand-name--back {
    fill: var(--ink);
    font-size: 36px;
  }
  .contact-line {
    font-family: "Open Sans", sans-serif;
    font-size: 18px;
    fill: var(--ink);
  }
  .zigzag-divider {
    fill: none;
    stroke: var(--ink-light);
    stroke-width: 1;
  }
  .chevron-band {
    fill: var(--ink);
  }
</style>
</head>
<body>
<svg class="stage" viewBox="0 0 1200 1000" xmlns="http://www.w3.org/2000/svg">
  <defs>
    <linearGradient id="quilt-tone" x1="0" y1="0" x2="1" y2="1">
      <stop offset="0" stop-color="#0d0d0d"/>
      <stop offset="0.5" stop-color="#1e1e1e"/>
      <stop offset="1" stop-color="#0a0a0a"/>
    </linearGradient>
    <linearGradient id="band-tone" x1="0" y1="0" x2="1" y2="0">
      <stop offset="0" stop-color="#050505"/>
      <stop offset="1" stop-color="#1a1a1a"/>
    </linearGradient>
  </defs>

  <!-- Front of card -->
  <g class="card card--front">
    <rect class="card-face" x="332.5" y="151.5" width="510" height="304"/>
    <polygon role="img" aria-label="Dark quilted diamond pattern panel"
      fill="url(#quilt-tone)"
      points="352,151 842,151 842,455 352,455 352,445 417,375 352,300 417,237"/>
    <text class="brand-name brand-name--front" x="613" y="323" text-anchor="middle">quarry5</text>
  </g>

  <!-- Back of card -->
  <g class="card card--back">
    <rect class="card-face" x="342.5" y="562.5" width="510" height="304"/>
    <polygon class="chevron-band" fill="url(#band-tone)"
      points="342,562 362,562 427,645 362,712 427,780 362,848 362,867 342,867"/>
    <text class="brand-name brand-name--back" x="486" y="727" text-anchor="middle">quarry5</text>

    <polyline class="zigzag-divider"
      points="580,625 585,634 577,643 585,652 577,661 585,670 577,679 585,688 577,697 585,706 577,715 585,724 577,733 585,742 577,751 585,760 577,769 585,778 577,787 585,796 580,805"/>

    <text class="contact-line" x="607" y="685">Website:quarry-5.com</text>
    <text class="contact-line" x="607" y="711">Email:info@quarry-5.com</text>
    <text class="contact-line" x="607" y="737">Name:lena moss</text>
    <text class="contact-line" x="607" y="763">Tel. +34 611 204 587</text>
  </g>
</svg>
</body>
</html>
```